Consultant Firm Marketing Flyer

I want to use this flyer to market health care consultant services. I would like a front and back glossy, professional, yet bold and eye catching design. I would like it to convey knowledge, expertise, partnership and strength. The colors should blue and white but I am very open to the designer being creative. You can visit my website to see colors and images I want to use at brightharborcare.net
I would like the home page image on my website to be incorporated into the flyer but I am also open to other images that work with the design. The designer can be creative.

I want to highlight 4 service area’s of focus to my clients:
1. Revenue Cycle Optimization (making my clients money)
2. Practice Management Optimization (improving clinical operations)
3. Health Compliance (following the law)
4. Health Care Technology: (Telemedicine and AI)
Please be creative. Go where ever your creativity leads.

```html
<!DOCTYPE html>
<html lang="en">
<head>
<meta charset="utf-8">
<title>Bright Harbor Care – Flyer</title>
<link href="https://fonts.googleapis.com/css2?family=Poppins:wght@500;600;700&family=Open+Sans:ital,wght@0,400;0,600;1,600&display=swap" rel="stylesheet">
<style>
:root{
  --stage:#8f8f8f;
  --white:#ffffff;
  --navy:#0a57a8;
  --deep:#0b4f9c;
  --sky:#2fa0d6;
  --sky-soft:#5bb8e6;
  --ink:#2b2b2b;
  --muted:#4a4a4a;
  --line:#c9d6e3;
}
*{margin:0;padding:0;box-sizing:border-box}
html,body{width:1200px;height:1000px;overflow:hidden;background:var(--stage)}
body{position:relative;font-family:"Open Sans",Arial,sans-serif;color:var(--ink)}
.page{position:absolute;background:var(--white);overflow:hidden}
.page--front{left:34px;top:138px;width:559px;height:723px}
.page--back{left:607px;top:138px;width:560px;height:724px}

.brand{position:absolute;display:flex;align-items:center;gap:7px;font-family:"Poppins",Arial,sans-serif;font-weight:600;color:var(--navy);font-size:12px;letter-spacing:.3px}
.brand__dot{width:16px;height:16px;border-radius:50%;background:var(--navy)}
.front .brand{left:0;right:0;top:40px;justify-content:center}

.hero{position:absolute;left:0;top:100px;width:559px;height:365px;background:linear-gradient(160deg,#c9ccd0 0%,#9a9ea4 45%,#6e6a6c 100%)}
.hero__url{position:absolute;left:0;right:0;top:103px;text-align:center;color:var(--white);font-family:"Poppins",Arial,sans-serif;font-size:11px;letter-spacing:2.4px;font-weight:500}
.hero__title{position:absolute;left:0;right:0;top:125px;text-align:center;color:var(--white);font-family:"Poppins",Arial,sans-serif;font-weight:600;font-size:36px;line-height:44px}

.name-band{position:absolute;left:0;top:467px;width:559px;height:42px;background:var(--sky);color:var(--white);font-family:"Poppins",Arial,sans-serif;font-weight:600;font-size:19px;text-align:center;line-height:42px}

.about__photo{position:absolute;left:36px;top:520px;width:126px;height:126px;border-radius:50%;background:linear-gradient(135deg,#e4e8ee,#9aa3ad)}
.about__text{position:absolute;left:196px;top:530px;width:320px;font-size:10.4px;line-height:13px;color:var(--muted)}
.about__lead{font-style:italic;font-weight:600;color:var(--ink);margin-bottom:9px}

.footer{position:absolute;left:0;top:657px;width:559px;height:66px;background:var(--navy);border-top:4px solid var(--sky);color:var(--white)}
.footer__call{position:absolute;left:36px;top:11px;display:flex;gap:10px}
.footer__label{font-size:13px;font-family:"Poppins",Arial,sans-serif}
.footer__phone{font-family:"Poppins",Arial,sans-serif;font-weight:600;font-size:18px;margin-top:-1px}
.footer__divider{position:absolute;left:236px;top:12px;height:42px;border-left:1px dashed rgba(255,255,255,.5)}
.footer__info{position:absolute;left:280px;top:11px;font-size:9.6px;line-height:13px}
.footer__info strong{font-size:11px;font-weight:600}
.footer__social{position:absolute;right:34px;top:30px;display:flex;gap:5px}
.footer__social span{width:12px;height:12px;border-radius:50%;background:var(--white)}

.back__photo{position:absolute;left:0;top:0;width:239px;height:724px;background:linear-gradient(180deg,#2aa6df 0%,#4bb3e3 40%,#1f8fd0 100%)}
.back__headline{position:absolute;right:25px;top:77px;text-align:right;color:var(--white);font-family:"Poppins",Arial,sans-serif;font-weight:600;font-size:19px;line-height:24px}
.back__accent{position:absolute;left:233px;top:82px;width:6px;height:60px;background:var(--navy)}
.back__contact{position:absolute;left:0;top:652px;width:239px;height:38px;background:rgba(255,255,255,.18);text-align:right;padding-right:26px;line-height:38px;font-family:"Poppins",Arial,sans-serif;font-weight:600;font-size:14px;color:var(--white)}
.back__contact b{color:var(--navy);font-weight:600}

.back .brand{left:274px;top:36px}
.solutions__title{position:absolute;left:275px;top:94px;font-family:"Poppins",Arial,sans-serif;font-weight:600;font-size:26px;color:var(--navy)}
.solutions__intro{position:absolute;left:275px;top:132px;width:250px;font-size:8px;line-height:11px;font-style:italic;font-weight:600;color:var(--ink)}

.service{position:absolute;left:298px;width:225px}
.service__title{font-family:"Poppins",Arial,sans-serif;font-weight:500;font-size:13px;color:var(--sky);margin-bottom:3px}
.service__text{font-size:8.3px;line-height:11px;color:var(--muted)}
.service__rule{position:absolute;left:298px;width:200px;border-top:1px dashed var(--line)}
.badge{position:absolute;left:190px;width:88px;height:88px;border-radius:50%;background:var(--white);display:flex;align-items:center;justify-content:center}
.badge__inner{width:76px;height:76px;border-radius:50%;background:var(--deep);display:flex;align-items:center;justify-content:center}

.back__address{position:absolute;left:275px;top:640px;font-size:8.6px;line-height:11.5px;color:var(--ink)}
.back__address strong{display:block;font-family:"Poppins",Arial,sans-serif;font-weight:500;font-size:11.5px;margin-bottom:1px}
.back__address b{color:var(--navy);font-weight:600}
</style>
</head>
<body>

<section class="page page--front front">
  <div class="brand"><span class="brand__dot"></span>Bright Harbor Care LLC</div>
  <div class="hero" role="img" aria-label="Photo of a healthcare team meeting around a table in a bright office">
    <p class="hero__url">www.brightharborcare.net</p>
    <h1 class="hero__title">Advancing Healthcare<br>Operations</h1>
  </div>
  <div class="name-band">Bright Harbor Care</div>
  <div class="about__photo" role="img" aria-label="Round photo of two consultants reviewing figures on a laptop"></div>
  <div class="about__text">
    <p class="about__lead">Bright Harbor Care (BHC) is a healthcare consulting firm skilled at helping physician practices advance their strategic vision in an ever-evolving healthcare system.</p>
    <p>Bright Harbor Care specializes in revenue cycle optimization, practice management improvement and developing new physician practices. Our technical skills allow us to dig deep into your revenue cycle while our strategic approach ensures we're keeping our eyes on the entire financial picture.</p>
  </div>
  <footer class="footer">
    <div class="footer__call">
      <svg width="14" height="14" viewBox="0 0 24 24" fill="none" stroke="#fff" stroke-width="1.8"><path d="M5 3h4l2 5-2.5 1.5a11 11 0 0 0 6 6L16 13l5 2v4a2 2 0 0 1-2 2A16 16 0 0 1 3 5a2 2 0 0 1 2-2z"/></svg>
      <div><div class="footer__label">CALL US:</div><div class="footer__phone">(555) 214-0387</div></div>
    </div>
    <div class="footer__divider"></div>
    <div class="footer__info">
      <strong>www.brightharborcare.net</strong><br>
      118 Harbor Ave, Portland, ME 04101, USA<br>
      Mail: <strong style="font-size:9.6px">info@brightharborcare.net</strong>
    </div>
    <div class="footer__social"><span></span><span></span><span></span></div>
  </footer>
</section>

<section class="page page--back back">
  <div class="back__photo" role="img" aria-label="Blue-toned photo of a doctor with a stethoscope using a tablet"></div>
  <h2 class="back__headline">Expertise Your<br>Medical Practice<br>Deserves</h2>
  <div class="back__accent"></div>
  <div class="back__contact">Contact <b>Us</b></div>

  <div class="brand"><span class="brand__dot"></span>Bright Harbor Care LLC</div>
  <h2 class="solutions__title">Solutions</h2>
  <p class="solutions__intro">The varied expertise of our team encompass full service revenue cycle management, practice management, regulatory compliance, human resource management, and full spectrum health care consulting services.</p>

  <div class="badge" style="top:196px"><div class="badge__inner">
    <svg width="34" height="34" viewBox="0 0 34 34" fill="none" stroke="#fff" stroke-width="2.2"><path d="M27 17a10 10 0 0 1-17 7"/><path d="M7 17a10 10 0 0 1 17-7"/><path d="M24 5v5h-5"/><path d="M10 29v-5h5"/></svg>
  </div></div>
  <div class="service" style="top:202px">
    <h3 class="service__title">Revenue Cycle Management</h3>
    <p class="service__text">In today's increasingly complex health care environment it's important now more than ever that medical practices closely manage their revenue cycle. Bright Harbor Care (BHC) understands the reimbursement landscape</p>
  </div>
  <div class="service__rule" style="top:293px"></div>

  <div class="badge" style="top:306px"><div class="badge__inner">
    <svg width="32" height="32" viewBox="0 0 32 32" fill="none" stroke="#fff" stroke-width="1.8"><rect x="7" y="4" width="18" height="24" rx="1"/><path d="M11 10h10M11 14h10M11 18h7M11 22h5"/><path d="M20 24l6-8 2 1.5-6 8-2.5 1z"/></svg>
  </div></div>
  <div class="service" style="top:312px">
    <h3 class="service__title">Regulatory Compliance</h3>
    <p class="service__text">In a heavily regulated healthcare environment medical practices need to be acutely aware of regulations as they present huge liabilities. It is extremely important to ensure compliance with regulations. BHC offers a host of comprehensive compliance services.</p>
  </div>
  <div class="service__rule" style="top:403px"></div>

  <div class="badge" style="top:416px"><div class="badge__inner">
    <svg width="32" height="32" viewBox="0 0 32 32" fill="none" stroke="#fff" stroke-width="1.8"><circle cx="10" cy="9" r="3.5"/><path d="M4 20a6 6 0 0 1 12 0"/><rect x="17" y="5" width="11" height="8" rx="1"/><path d="M19 8h7M19 11h5"/><circle cx="20" cy="19" r="3"/><path d="M15 29a5 5 0 0 1 10 0"/></svg>
  </div></div>
  <div class="service" style="top:422px">
    <h3 class="service__title">Human Resource Management</h3>
    <p class="service__text">Do you need Human Resources Management but don't want the expense of a full service Human Resources Department? Not having a full service Human Resources Department can increase liability and be costly to your medical practice.</p>
  </div>
  <div class="service__rule" style="top:513px"></div>

  <div class="badge" style="top:526px"><div class="badge__inner">
    <svg width="32" height="32" viewBox="0 0 32 32" fill="none" stroke="#fff" stroke-width="1.8"><path d="M16 16V4M12 8l4-4 4 4"/><path d="M8 18V9M5 12l3-3 3 3"/><path d="M24 18V9M21 12l3-3 3 3"/><circle cx="9" cy="22" r="2.2"/><circle cx="16" cy="21" r="2.2"/><circle cx="23" cy="22" r="2.2"/><path d="M5 29a4 4 0 0 1 8 0M12 28a4 4 0 0 1 8 0M19 29a4 4 0 0 1 8 0"/></svg>
  </div></div>
  <div class="service" style="top:532px">
    <h3 class="service__title">Practice Management</h3>
    <p class="service__text">Practice Management is challenging and it requires the right balance of skill, knowledge, experience and management expertise. BHC Offers assessment and optimization in Patient Access &amp; Scheduling, Patient Experience, Staff Experience.</p>
  </div>

  <div class="back__address">
    <strong>Bright Harbor Care</strong>
    118 Harbor Ave, Portland, ME 04101, USA<br>
    Phone: <b>(555) 214-0387</b><br>
    Website: www.brightharborcare.net<br>
    Mail: info@brightharborcare.net
  </div>
</section>

</body>
</html>
```